HollowPine Ventures Inc. Business Card Design

My business is custom renovations and homes.I would need to have a new business logo created to go along with my company name. The business card should be of a modern style as this is the market I am focused on. I would need my contact information and website posted on the card. I would also like to list a few of the tasks I conduct on the card (such as: Renovations, Additions, Repairs, New Homes, Design, Consultations). On the reverse of the card I currently have just my logo and my motto, "Shaping A Bold Path". However, I am open to completely changing everything as I am starting a new year and would like to excel further. Any new ideas and suggestions are always welcomed. Thank you.

Target Market(s)

Upscale residential and commercial renovations and builds

Industry/Entity Type

Business

Contact Information for Business Card

I would like the design to be able to be laser cut or burnt onto a wooden business card. I will be creating one option of cards for really loyal customers (wooden) and a second option for the everyday customer (paper).

Font styles to use
Other font styles liked:
• Calibri / anything of mordern taste

Colors
f37122
5c5c5c
474747
ffffff

Requirements
Must have
• I would like the colours of my business to be a sharp orange and grey. I believe this will symbolize a modern style. I am open to other suggestions if this is not suitable for the designers tastes. My contact info as follows:
• Will Marsh
• President
• HollowPine Ventures Inc.
• 555-214-3987
• will@hollowpineventures.example
• I would like my website (currently under construction) hollowpineventures.example on the card aswell.
Nice to have
• Along with a modern logo representing HollowPine, I would like something on the card besides the logo and contact information. Perhaps a small background design. I feel it may be nice to have my services listed on the card (in smaller font on the bottom) Renovations, Additions, Repairs, Design, Consultations.
Should not have
• The business card should not have too many different colors. Should not have rounded corners.

```html
<!DOCTYPE html>
<html lang="en">
<head>
<meta charset="utf-8">
<title>HollowPine Ventures Inc. — Business Card</title>
<link rel="stylesheet" href="https://fonts.googleapis.com/css2?family=Open+Sans:wght@400;600;700&display=swap">
<style>
  :root {
    --orange: #f37122;
    --grey-light: #5c5c5c;
    --grey-dark: #474747;
    --white: #ffffff;
    --backdrop: #e4e4e4;
    --wood-a: #3a3a3a;
    --wood-b: #555555;
    --wood-c: #2e2e2e;
  }
  * { margin: 0; padding: 0; box-sizing: border-box; }
  html, body {
    width: 1200px; height: 987px; overflow: hidden;
    background: var(--backdrop);
    font-family: "Open Sans", sans-serif;
  }
  .canvas { position: relative; width: 1200px; height: 987px; }
  .card {
    position: absolute; left: 293px; width: 615px; height: 350px;
    overflow: hidden;
  }
  .card--front { top: 130px; }
  .card--back { top: 505px; }
  .card__texture {
    position: absolute; inset: 0;
    background: linear-gradient(100deg, var(--wood-c) 0%, var(--wood-b) 35%, var(--wood-a) 60%, var(--wood-b) 82%, var(--wood-c) 100%);
  }
  .brand { position: absolute; left: 127px; top: 74px; display: flex; align-items: flex-start; gap: 12px; }
  .brand__square { width: 30px; height: 30px; background: var(--orange); margin-top: 16px; }
  .brand__name { color: var(--white); font-weight: 600; font-size: 46px; line-height: 1.05; letter-spacing: -0.5px; }
  .brand__suffix { display: block; font-size: 32px; }
  .person { position: absolute; right: 386px; top: 160px; text-align: right; }
  .person__name { color: var(--orange); font-weight: 600; font-size: 21px; line-height: 1.2; }
  .person__title { color: var(--white); font-size: 16px; line-height: 1.3; }
  .divider { position: absolute; left: 246px; top: 152px; width: 1px; height: 57px; background: #8a8a8a; }
  .contacts { position: absolute; left: 274px; top: 150px; list-style: none; }
  .contacts li { display: flex; align-items: center; gap: 7px; height: 23.5px; color: var(--white); font-size: 16px; }
  .contacts svg { width: 14px; height: 14px; fill: var(--orange); flex: none; }
  .services {
    position: absolute; left: 0; right: 0; top: 236px; text-align: center;
    color: var(--orange); font-weight: 600; font-size: 16px;
  }
  .back-name {
    position: absolute; left: 0; right: 0; top: 120px; text-align: center;
    color: var(--orange); font-weight: 700; font-size: 60px; line-height: 1;
  }
  .motto {
    position: absolute; left: 0; right: 0; top: 294px; text-align: center;
    color: var(--orange); font-weight: 600; font-size: 18px;
  }
</style>
</head>
<body>
<main class="canvas">
  <section class="card card--front" aria-label="Business card front">
    <div class="card__texture" role="img" aria-label="Dark grey weathered wood plank texture"></div>
    <div class="brand">
      <span class="brand__square" aria-hidden="true"></span>
      <p class="brand__name">HollowPine<span class="brand__suffix">Ventures Inc.</span></p>
    </div>
    <div class="person">
      <p class="person__name">Will Marsh</p>
      <p class="person__title">President</p>
    </div>
    <span class="divider" aria-hidden="true"></span>
    <ul class="contacts">
      <li><svg viewBox="0 0 24 24" aria-hidden="true"><path d="M6.6 10.8a15.1 15.1 0 0 0 6.6 6.6l2.2-2.2c.3-.3.7-.4 1-.2 1.1.4 2.3.6 3.6.6.6 0 1 .4 1 1V20c0 .6-.4 1-1 1A17 17 0 0 1 3 4c0-.6.4-1 1-1h3.5c.6 0 1 .4 1 1 0 1.3.2 2.5.6 3.6.1.3 0 .7-.2 1z"/></svg>555-214-3987</li>
      <li><svg viewBox="0 0 24 24" aria-hidden="true"><path d="M2 5h20v14H2z M2 5l10 8 10-8" /></svg>will@hollowpineventures.example</li>
      <li><svg viewBox="0 0 24 24" aria-hidden="true"><path d="M12 2a10 10 0 1 0 0 20 10 10 0 0 0 0-20zm0 2c1 0 2.3 2.2 2.8 6H9.2C9.7 6.2 11 4 12 4zm-7.9 8c0-.7.1-1.3.3-2h2.9a20 20 0 0 0 0 4H4.4a8 8 0 0 1-.3-2zm5.1 2a18 18 0 0 1 0-4h5.6a18 18 0 0 1 0 4zm2.8 6c-1 0-2.3-2.2-2.8-4h5.6c-.5 1.8-1.8 4-2.8 4zm4.8-6a20 20 0 0 0 0-4h2.9a8 8 0 0 1 0 4z"/></svg>hollowpineventures.example</li>
    </ul>
    <p class="services">Renovations | Additions | Repairs | Design | Consultations.</p>
  </section>

  <section class="card card--back" aria-label="Business card back">
    <div class="card__texture" role="img" aria-label="Dark grey weathered wood plank texture"></div>
    <p class="back-name">HollowPine</p>
    <p class="motto">Shaping A Bold Path</p>
  </section>
</main>
</body>
</html>
```